Verdant QUICK Repairs Business card

Harbison Motors is looking for a business card design for our detailing wing "Verdant QUICK Repairs"
The services offered are vehicle paintless dent repairs, vehicle detailing, scratch and bumper repairs & paint and alloy wheel repairs.
Ideally the card design should be sharp, neat and professional. We are not looking for a card with pictures of cars.
Our corporate colours are blues (as in the logo supplied) which may look good with water droplets in high res and perhaps one or two images leaking off the card. Dark blacks with electric blues perhaps.
Images may be of a spray gun (we use Carrowmist), a rotary polisher (Trevalo Orbix) or similar objects used in the processes.

Industry/Entity Type

Paint

Contact Information for Business Card

Title: Verdant QUICK Repairs
Services: Bumper Repairs
Scratch/Paint Repairs
Paintless dent repairs
Alloy wheel repairs
Name: Martin K
Telephone: 0427195063
Email : martin@harbisonmotors.com.au

Font styles to use
Sans Serif
Other font styles liked:

Colors
0355a3
3277b5
0792cd
cfdfed

Requirements
Must have
• The title - "Verdant QUICK Repairs" should be a focus on either the from or back of the card
Should not have
• Photographs of cars

```html
<!DOCTYPE html>
<html lang="en">
<head>
<meta charset="utf-8">
<title>Verdant QUICK Repairs – Business Card</title>
<link rel="stylesheet" href="https://fonts.googleapis.com/css2?family=Open+Sans:wght@400;600;700;800&display=swap">
<style>
  :root {
    --navy: #1b2a6b;
    --brand-blue: #0355a3;
    --mid-blue: #3277b5;
    --electric-blue: #0792cd;
    --ice-blue: #cfdfed;
    --card-white: #fbfbfb;
    --stage: #3a3431;
    --ink: #1c2550;
  }
  * { box-sizing: border-box; margin: 0; padding: 0; }
  html, body {
    width: 1200px; height: 768px; overflow: hidden;
    background: var(--stage);
    font-family: "Open Sans", Arial, sans-serif;
  }
  .canvas {
    position: relative; width: 1200px; height: 768px;
  }
  .card {
    position: absolute; top: 224px;
    width: 540px; height: 320px;
    background: var(--card-white);
    overflow: hidden;
    box-shadow: 0 10px 24px rgba(0,0,0,.35);
  }
  .card--front { left: 40px; }
  .card--back  { left: 620px; }

  /* Wordmark stand-in */
  .wordmark {
    position: absolute; display: flex; align-items: center; gap: 12px;
    color: var(--navy); font-weight: 800; letter-spacing: .5px;
  }
  .wordmark__dot {
    width: 30px; height: 30px; border-radius: 50%;
    background: var(--navy); flex: none;
  }
  .card--front .wordmark { left: 90px; top: 100px; font-size: 40px; }
  .card--front .wordmark__dot { width: 44px; height: 44px; }
  .card--back .wordmark { left: 36px; top: 40px; font-size: 26px; }

  /* Front services band */
  .services-band {
    position: absolute; left: 0; right: 0; bottom: 0; height: 52px;
    background: var(--navy); color: #fff;
    display: flex; align-items: center; padding-left: 22px;
    font-size: 16px; font-weight: 400;
  }

  /* Back details */
  .details { position: absolute; left: 250px; top: 130px; color: var(--ink); }
  .details__title {
    color: var(--brand-blue); font-size: 20px; font-weight: 700;
    letter-spacing: .3px; margin-bottom: 12px;
  }
  .details__name { font-size: 15px; font-weight: 700; color: var(--navy); }
  .details__role { font-size: 12px; margin-bottom: 14px; }
  .contact-list { list-style: none; font-size: 14px; }
  .contact-list li { display: flex; align-items: center; gap: 10px; line-height: 22px; }
  .contact-list svg { width: 13px; height: 13px; fill: var(--brand-blue); flex: none; }

  .back-accent { position: absolute; left: 0; bottom: 0; width: 540px; height: 100px; }
</style>
</head>
<body>
<main class="canvas">

  <section class="card card--front" aria-label="Card front">
    <div class="wordmark"><span class="wordmark__dot"></span>Harbison Motors</div>
    <p class="services-band">Repairing of: Bumper, Scratch/Paint, Paintless dent, Alloy wheel</p>
  </section>

  <section class="card card--back" aria-label="Card back">
    <div class="wordmark"><span class="wordmark__dot"></span>Harbison Motors</div>

    <div class="details">
      <h1 class="details__title">Verdant QUICK Repairs</h1>
      <p class="details__name">Martin K</p>
      <p class="details__role">Managing Director</p>
      <ul class="contact-list">
        <li>
          <svg viewBox="0 0 16 16" aria-hidden="true"><path d="M3 1h3l1.5 4-2 1.2a9 9 0 0 0 4.3 4.3L11 8.5l4 1.5v3a2 2 0 0 1-2 2A12 12 0 0 1 1 3a2 2 0 0 1 2-2z"/></svg>
          0427195063
        </li>
        <li>
          <svg viewBox="0 0 16 16" aria-hidden="true"><path d="M1 3h14v10H1z M1 3l7 6 7-6" stroke="#fff" stroke-width="1.2"/></svg>
          martin@harbisonmotors.com.au
        </li>
        <li>
          <svg viewBox="0 0 16 16" aria-hidden="true"><circle cx="8" cy="8" r="7"/><path d="M1 8h14M8 1c-3 4-3 10 0 14M8 1c3 4 3 10 0 14" stroke="#fff" stroke-width="1" fill="none"/></svg>
          www.harbisonmotors.com.au
        </li>
      </ul>
    </div>

    <svg class="back-accent" viewBox="0 0 540 100" aria-hidden="true">
      <polygon points="0,40 540,100 0,100" fill="var(--navy)"/>
      <polygon points="0,52 540,112 540,100 0,100" fill="var(--navy)"/>
      <polygon points="340,100 540,62 540,100" fill="var(--electric-blue)"/>
      <polygon points="330,100 360,92 380,100" fill="#fff" opacity="0"/>
    </svg>
  </section>

</main>
</body>
</html>
```